New Discover Site!!

Hello everyone!
We're WanderlyTrips. A tour company which offer group excursions to places like Morocco & Portugal for young adults. We have been in the business for 10 years now and we'd like to create a new fresh look and feel design. Something clean and more modern.
We offer trips to:
1 - Weekend trips Lagos, Portugal
2 - Weekend tips to Morocco
3 - 5 day trip to the Sahara Desert in Morocco
4 - Beach day trips to Cadiz
5 - Day trip to Gibraltar
6 - Costume trips
7 - Wine Tasting day trip
8 - Fiestas de Marvela
Those are the 8 boxes we'd like to have on our home-page along with an awesome header and footer. You can take a look for our current page to see sections and the text of the sections. Once we approve a nice home page from any of you designers, we will go ahead and send you the names of all the pages we'd like you to design for us. We already have someone who will code all the pages. We just need a new design for all the pages.
You can see our logo on our Blog: http://wanderlytripsblog.example/
We like websites like:
www.Holvaro.com
www.Skarnel.com
We look forward to hear from you!!
PS:
we will need the home page and other pages.
7 pages plus 8 trip pages. The trip pages they can all look the same (design wise) obviusly diferent photos, video and content. Total 15 pages.
Page 1 - Home page
Page 2 - About us. This page can look similar to:
Page 3 - FAQs. This page can look similar to:
Page 4 - Contact us. This page can look similar to: http://www.holvaro.com/contact
Page 5 - Trip check in. This page can look similar to the Skarnel.com look for flight check in. Something clean.
Page 6 - Trip videos. This page, will have the list of all our trip videos. A line or two of the trip and the video right below.
Page 7 - Trip departure info. On this page we're going to have the information on how to get to Sevilla. Also the google map of the actual meeting point and maybe a youtube video somewhere.
Page 8 - Why travel with us.
How many trip page are we going to need?
We have 8 trips. If you can just do 1 page, then you can do the same type page for all the trips. On each trip page you must add the following content:
Trip overview
Whats included
Trip dates
Photos and a youtube video.
An example of our current lagos trip page is:
https://www.wanderlytrips.example/2001/09/beach-getaway-lagos-portugal/
You can take all the content from www.WanderlyTrips.example

```html
<!DOCTYPE html>
<html lang="en">
<head>
<meta charset="utf-8">
<title>Lagos Trip – WanderlyTrips</title>
<link rel="stylesheet" href="https://fonts.googleapis.com/css2?family=Source+Sans+3:wght@400;600;700&display=swap">
<style>
:root{
  --red:#b8111a;
  --red-dark:#8f0a10;
  --gold:#f3b200;
  --text:#4a4a4a;
  --heading:#2b2b2b;
  --rule:#dddddd;
  --page-bg:#eeeeee;
  --panel:#ffffff;
  --footer:#3a3a3a;
  --footer-deep:#2e2e2e;
  --footer-text:#e6e6e6;
  --footer-line:#555555;
}
*{box-sizing:border-box;margin:0;padding:0}
html,body{width:1200px;height:2695px;overflow:hidden}
body{position:relative;background:var(--page-bg);font-family:"Source Sans 3",Arial,sans-serif;color:var(--text);font-size:13px;line-height:20px}
a{color:inherit;text-decoration:none}

.site-header{position:absolute;left:0;top:0;width:1200px;height:122px;background:var(--panel);border-top:4px solid #3b1a1a;border-bottom:1px solid var(--rule)}
.brand{position:absolute;left:96px;top:24px;display:flex;align-items:center;gap:10px}
.brand-mark{width:26px;height:26px;border-radius:50%;background:var(--red)}
.brand-name{font-size:26px;font-weight:700;color:var(--heading);letter-spacing:.2px}
.utility{position:absolute;left:727px;top:5px;width:370px;height:40px;background:#f0f0f0;display:flex;align-items:center;justify-content:center;font-size:13px;color:#555}
.utility a{padding:0 9px;border-left:1px solid #999;line-height:13px}
.utility a:first-child{border-left:0}
.main-nav{position:absolute;right:101px;top:80px;display:flex;gap:31px;font-size:16px;font-weight:700;color:var(--red);text-transform:uppercase}

.hero{position:absolute;left:77px;top:122px;width:1047px;height:323px;background:linear-gradient(180deg,#cfe6f6 0%,#e9f3fa 55%,#f7f3ea 100%)}

.content{position:absolute;left:77px;top:445px;width:1051px;height:1908px;background:var(--panel);box-shadow:0 0 6px rgba(0,0,0,.06);padding:0 38px}
.page-title{position:absolute;left:38px;top:34px;font-size:27px;font-weight:600;color:var(--red)}
.section-title{font-size:20px;font-weight:600;color:var(--heading);position:absolute}
.photo{position:absolute;border-radius:3px}
.rule{position:absolute;left:38px;width:973px;height:1px;background:var(--rule)}
.prose p{margin-bottom:9px}

.overview-photo{left:38px;top:114px;width:215px;height:163px;background:linear-gradient(135deg,#c89a62 0%,#d8b27b 40%,#4fb6c6 70%,#2a8aa5 100%)}
.overview-text{position:absolute;left:271px;top:112px;width:740px;font-size:12.5px;line-height:20.5px}

.price-photo{left:38px;top:395px;width:221px;height:97px;background:linear-gradient(135deg,#2c2c3a,#5b4a8a 60%,#8c86b8)}
.total{position:absolute;left:42px;top:502px;width:217px;display:flex;justify-content:space-between;align-items:center;font-size:15px}
.total strong{font-size:26px;font-weight:400;color:var(--red)}
.dates{position:absolute;left:386px;top:397px;width:221px;height:171px;border-radius:6px;background:linear-gradient(180deg,var(--red),var(--red-dark));padding:12px 0 0 24px;list-style:none;font-size:13px;font-weight:700;color:#fff}
.dates li{display:flex;height:32px;align-items:center}
.dates .month{width:72px;color:var(--gold)}

.included{position:absolute;left:38px;top:680px;width:990px;list-style:none;font-size:13px}
.included li{margin-bottom:11px}

.optional-title{position:absolute;left:44px;top:1068px;font-size:16px;font-weight:600;color:var(--red)}
.activity{position:absolute;top:1100px;font-size:13px}
.activity h3{font-size:17px;font-weight:400;color:var(--heading);margin-bottom:10px}
.activity p{margin-bottom:10px;line-height:21px}
.activity.sail{left:45px;width:431px}
.activity.surf{left:526px;width:437px}
.col-divider{position:absolute;left:492px;top:1108px;width:1px;height:228px;background:var(--rule)}
.note{position:absolute;left:46px;top:1345px;font-size:13px;color:var(--red)}

.itinerary{position:absolute;left:38px;top:1475px;width:980px;font-size:13px}
.itinerary p{margin-bottom:11px}

.gallery .photo{top:1667px;width:213px;height:131px}
.g1{left:43px;background:linear-gradient(180deg,#8fb7c4,#4a7a6b)}
.g2{left:279px;background:linear-gradient(135deg,#4fb8d6,#d9b15b 60%,#2d93b8)}
.g3{left:507px;background:linear-gradient(180deg,#cfc2a6,#7d7a6e)}
.g4{left:756px;background:linear-gradient(135deg,#7fc8e4,#ffffff 55%,#f1a33a)}

.footer-icons{position:absolute;top:2328px;height:25px;background:var(--footer);border-radius:4px 4px 0 0}
.site-footer{position:absolute;left:0;top:2353px;width:1200px;height:260px;background:var(--footer);color:var(--footer-text)}
.footer-col{position:absolute;top:38px;height:170px;padding-left:0}
.footer-col h4{font-size:20px;font-weight:400;color:#fff;margin-bottom:12px}
.footer-col ul{list-style:none;font-size:13px;line-height:24.6px}
.footer-col.split{border-left:1px solid var(--footer-line);padding-left:0}
.social{display:flex;gap:6px;margin-top:4px}
.social span{width:25px;height:25px;border-radius:50%;background:#f4f4f4}
.legal{position:absolute;left:0;top:2613px;width:1200px;height:82px;background:var(--footer-deep);color:#9a9a9a;font-size:12px;padding:22px 0 0 101px}
</style>
</head>
<body>

<header class="site-header">
  <a class="brand" href="#"><span class="brand-mark"></span><span class="brand-name">WanderlyTrips</span></a>
  <nav class="utility">
    <a href="#">Register</a><a href="#">Sign In</a><a href="#">Newsletters</a><a href="#">Support</a><a href="#">Contact</a>
  </nav>
  <nav class="main-nav">
    <a href="#">Home</a><a href="#">Tours</a><a href="#">Who we are</a><a href="#">Latest deals</a><a href="#">Book now</a><a href="#">Special offers</a><a href="#">Resouces</a>
  </nav>
</header>

<div class="hero" role="img" aria-label="Travel collage of an airliner, famous world landmarks, hot-air balloons and seagulls over a sky-blue background"></div>

<main class="content">
  <h1 class="page-title">Lagos Trip</h1>

  <h2 class="section-title" style="left:38px;top:80px">Overview</h2>
  <div class="photo overview-photo" role="img" aria-label="Golden sea cliffs above a turquoise cove in Lagos"></div>
  <div class="overview-text prose">
    <p>At just a stone's throw away, Lagos is the perfect destination for that weekend beach getaway you've been craving since you first stepped on European soil. Boasting some of the most breathtaking beaches, mouth-watering meals, and absolutely insane parties, Lagos easily proves itself to be one of Europe's best hidden treasures. It's truly become our pleasure to show our travelers how and why it's so easy to fall in love with everything that Lagos has to offer.</p>
    <p>With an abundance of activities from sangria sailboat cruises to surf lessons to couch-tubing and jet skiing, as well with mini-excursions to Sagres to see the sun set at the stunning "End of the World," and free time to explore the city for yourself, Lagos may very well become the greatest weekend of your life, and that's no lie. This trip is the perfect way to treat yourself to that beach get-away you've been wanting and needing for far too long.</p>
  </div>

  <div class="rule" style="top:333px"></div>

  <h2 class="section-title" style="left:38px;top:358px">Trip Price</h2>
  <div class="photo price-photo" role="img" aria-label="Hand holding a travel ticket"></div>
  <div class="total"><span>Total Price</span><strong>139€</strong></div>

  <h2 class="section-title" style="left:386px;top:358px">Trip Dates</h2>
  <ul class="dates">
    <li><span class="month">JUNE</span>7TH – 9TH</li>
    <li><span class="month">JUNE</span>14TH – 16TH</li>
    <li><span class="month">JUNE</span>21ST – 23RD</li>
    <li><span class="month">JUNE</span>28TH – 30TH</li>
    <li><span class="month">JULY</span>5TH – 7TH</li>
  </ul>

  <div class="rule" style="top:618px"></div>

  <h2 class="section-title" style="left:38px;top:642px">What's included</h2>
  <ul class="included">
    <li>A comfortable roundtrip bus ride from Sevilla to Lagos with air-conditioning, music, and movies tailored just for you.</li>
    <li>3 days and 2 night in one of the top hotels in all of Lagos, just minutes away from the beach, complete with spacious rooms, buffet-style breakfasts, and a beautiful outdoor pool.</li>
    <li>Three gorgeous beaches to lay out on &amp; soak in the warm rays: Praia Dona Ana, Meia Praia, &amp; Praia do Amado.</li>
    <li>Beach games, music, and sangria during the day.</li>
    <li>Exclusive VIP parties set up just for WanderlyTrips travelers every night at the top bars/clubs in Lagos with drink specials &amp; surprises all night long.</li>
    <li>A mini-excursion to Sagres to watch a stunning sunset at what was once considered "The End of the World."</li>
    <li>A tour of the breathtaking cliffs at Ponte da Piedade.</li>
    <li>A special WanderlyTrips wristband that will get you discounts in countless restaurants and bars throughout Lagos.</li>
    <li>Free time to explore and get a feel for Lagos on your own.</li>
    <li>English-speaking guides available at all times to show you the very best spots in Lagos and answer any questions that you may have.</li>
    <li>Optional activities – Sangria Sailboat Cruise &amp; Surfing.</li>
  </ul>

  <h3 class="optional-title">Optional Activities:</h3>
  <div class="activity sail">
    <h3>Sangria Sailboat Cruise</h3>
    <p>Cruise down the beautiful coast of Lagos sailing slowly on the breeze as you sip on homemade Portuguese sangria and listen to the sweet tunes of summer.</p>
    <p>On this 2 hour cruise, you will be taken by a smaller boat to see the wondrous naturally-formed grottos &amp; caves that have become so famous over the years, and will have ample time to sunbathe, jump off the sail-boat for a swim, or simply sit and sip in the good times under the warm Portuguese sun.</p>
  </div>
  <div class="col-divider"></div>
  <div class="activity surf">
    <h3>Surfing lessons</h3>
    <p>Ever wanted to learn how to surf? Well here's your chance to finally make that dream become an unbelievable reality, and on one of the most famous beaches in all of Portugal too – Praia do Amado.</p>
    <p>Our Surfing excursion includes a 2 hour professional lesson in which you learn everything from the basics to standing up on your very first wave (surfboard &amp; wetsuit included).</p>
  </div>
  <p class="note">Note: You will be able to sign up for these activities on the bus to Lagos as well as at the hotel upon checking in.</p>

  <div class="rule" style="top:1410px"></div>

  <h2 class="section-title" style="left:38px;top:1436px">Trip itinerary</h2>
  <div class="itinerary">
    <p>A copy of the actual itinerary will be sent you by you automatically right after signed up online! You can log in into the website and check your trip status and download a copy of the trip itinerary J Buses depart from Sevilla around 10AM, unless specified on our website. In summer time, we usually depart from Sevilla around 3PM. Please feel free to talk to us via our live chat and we will let you know the exact time. We usually return back to Sevilla around 9:45PM.</p>
    <p>Buses will stop at the same place of departure 'Consulado de Portugal'</p>
  </div>

  <div class="rule" style="top:1606px"></div>

  <h2 class="section-title" style="left:38px;top:1630px">Photos all around</h2>
  <div class="gallery">
    <div class="photo g1" role="img" aria-label="Friends leaping into a lake"></div>
    <div class="photo g2" role="img" aria-label="Sunbather in a straw hat floating in clear water"></div>
    <div class="photo g3" role="img" aria-label="Travelers taking a photo in a historic square"></div>
    <div class="photo g4" role="img" aria-label="Cocktail on a sunny beach lounger"></div>
  </div>
</main>

<div class="footer-icons" style="left:132px;width:40px" role="img" aria-label="Airplane icon"></div>
<div class="footer-icons" style="left:715px;width:58px" role="img" aria-label="Cruise ship icon"></div>
<div class="footer-icons" style="left:1052px;width:38px" role="img" aria-label="Palm tree icon"></div>

<footer class="site-footer">
  <div class="footer-col" style="left:101px">
    <h4>Company</h4>
    <ul><li>Ou Mission</li><li>Why Choose Us</li><li>Testimonials</li><li>Recent Blog Posts</li><li>Newsletters</li></ul>
  </div>
  <div class="footer-col split" style="left:245px;width:0"></div>
  <div class="footer-col" style="left:298px">
    <h4>Book Your Tours</h4>
    <ul><li>Find Your Tour</li><li>Book Now</li><li>Why Choose Us</li><li>Latest Offers</li><li>Best Tours</li></ul>
  </div>
  <div class="footer-col split" style="left:471px;width:0"></div>
  <div class="footer-col" style="left:515px">
    <h4>Your Booking</h4>
    <ul><li>My Reservation</li><li>Check-in online</li><li>Change your flight</li><li>Lock your price</li></ul>
  </div>
  <div class="footer-col split" style="left:668px;width:0"></div>
  <div class="footer-col" style="left:715px">
    <h4>Customer Support</h4>
    <ul><li>Our Support</li><li>Enquiry Now</li><li>Chat Now</li><li>FAQ's</li><li>Term &amp; Use</li></ul>
  </div>
  <div class="footer-col split" style="left:900px;width:0"></div>
  <div class="footer-col" style="left:941px">
    <h4>Get Connected</h4>
    <div class="social" aria-label="Social links"><span></span><span></span><span></span><span></span></div>
  </div>
</footer>

<div class="legal">© 2012 Company Name.&nbsp; All right reserved.&nbsp; Term of Use</div>

</body>
</html>
```